CODED website - Breakfree418

I am a successful entrepreneur - have recently sold my business and am semi-retired. I want to give something back, as well as provide a blog for articles and my journeys.

I will also be using this to provide free business and entrepreneurial advice.

I am creating a NOT FOR PROFIT business called Breakfree418.com.au which will provide the following;

1. Blog and articles; my travels, Small to Medium business advice and articles

2. My Bucket List - the 100 things I aim to achieve

3. Free business / start up advice - a section on the website which provides case studies on people / businesses which ask me for advice. We will then chronicle their story and what advice we have given for them to succeed.

My inspiration is the Martin Okonkwo idea and website;

http://martinokonkwo.example/about-martin/

Obviously I do NOT want a copy of this site, but use this for inspiration.

Furthermore, I would be interested in ongoing collaboration with the successful designer - I will be providing advice and consultancy to start ups, all of which will need web design etc, so there is ongoing referral streams for the successful designer.

I need this to be CODED and then uplifted to the website, so please DO NOT bid on this unless you can provide a coded site and facilitate the upload to WildHostings.

The NECESSARY tabs / pages

Main landing page - a short introduction into the ethos of Breakfree418

Writing - this will be the blog articles

About

Our Bucket List - a section where we can add our 100 buket list items. Hyperlinked to open a new page which has details on each bucket list item (ie #1 Make Breakfree418 - hyperlink to a new page which then has info on the bucklist item and what we have done)

Breakfree418 - this will be the section where we discuss people / businesses that we are helping. We will have an opening intro section + a link to the contact us page so they can ask us for the free advice. This will be the section where we have case studies into businesses / people that we have helped.
Updates

Hey everyone!

I'm really keen to get this website launched and looking amazing - if you have any questions, or would like to discuss anything at all, please email me at

dave@pinnaclepost.example.au

As I mentioned in the brief, I am doing this site to give back; I will not be earning a cent, and I will not be trying to earn any funds. I'm doing it simply to help other start ups or entrepreneurs, so I really want this site to look amazing.

I hope someone reads this and is inspired, and wants to be involved in this social enterprise with me.

Really excited to hear from you all and see your designs!

Industry/Entity Type

Business

Requirements
Must have
• MUST BE CODED and uplifted to the WildHosting registered domain - www.breakfree418.com.au - happy to discuss additional costings for this with successful designer.

Separate pages for each section (as outlined in the brief above)

Blog section to look similar to http://martinokonkwo.example/3x5/

Comprehensive website - not a simple wordpress template theme with some minor modifications. I will immediately reject any simple template design. I am looking for a slick, fully functioning website design.

PLEASE BE AWARE that I am looking for ongoing collaboration with the www.breakfree418.com.au.

I am trying this website as I want to find a young, energetic, vibrant, dynamic designer - this is your opportunity to be a part of something big, as this website will be huge!

Please do not submit a design if you are not motivated and ready for something big.

```html
<!DOCTYPE html>
<html lang="en">
<head>
<meta charset="utf-8">
<title>Breakfree418</title>
<link href="https://fonts.googleapis.com/css2?family=Arvo:wght@700&family=Oswald:wght@700&family=Arimo:wght@400;700&display=swap" rel="stylesheet">
<style>
:root{
  --page:#e6e2d9;
  --sheet:#f2f2f2;
  --ink:#333;
  --body:#555;
  --muted:#999;
  --dark:#2f2f2f;
  --link:#2a9fd6;
  --red:#cc2020;
  --line:#dcdcdc;
  --foot:#e9e6df;
  --bar:#cfcfcf;
}
*{margin:0;padding:0;box-sizing:border-box}
html,body{width:753px;height:1200px;overflow:hidden}
body{background:var(--page);font-family:"Arimo",sans-serif;color:var(--body);position:relative}
.abs{position:absolute}
.sheet{left:62px;top:0;width:628px;height:1052px;background:var(--sheet);box-shadow:0 0 6px rgba(0,0,0,.15)}
.brand{left:78px;top:14px;font:700 24px/1 "Oswald",sans-serif;color:#555;letter-spacing:.3px}
.nav{top:26px;font:700 10px/1 "Arvo",serif;color:var(--ink)}
.nav.current{color:#aaa}
.nav-flag{left:366px;top:0;width:12px;height:18px;background:#bbb;clip-path:polygon(0 0,100% 0,100% 100%,50% 75%,0 100%)}
.panel{background:#fafafa;border:1px solid var(--line)}
.photo{background:linear-gradient(160deg,#3a2418 0%,#b5703a 45%,#e6b070 70%,#2a1a10 100%)}
.dot{top:222px;width:10px;height:10px;background:#888;color:#fff;font:8px/10px "Arimo",sans-serif;text-align:center}
.dot.on{background:#555}
.bucket-tab{left:726px;top:86px;width:27px;height:95px;background:var(--dark);border-radius:3px 0 0 3px}
.bucket-tab span{position:absolute;left:5px;top:90px;transform:rotate(-90deg);transform-origin:0 0;white-space:nowrap;color:#fff;font:700 11px/1 "Arimo",sans-serif}
.h1{font:700 18px/1 "Arvo",serif;color:var(--ink)}
.ribbon{width:12px;height:27px;background:var(--dark);clip-path:polygon(0 0,100% 0,100% 100%,50% 78%,0 100%)}
.copy{font-size:8px;line-height:15.2px;text-align:justify;color:var(--body)}
.more{left:62px;width:58px;height:16px;background:var(--dark);color:#fff;font:8px/16px "Arimo",sans-serif;padding-left:8px;clip-path:polygon(0 0,100% 0,92% 50%,100% 100%,0 100%)}
.card{width:128px;height:158px;background:var(--dark)}
.card .img{position:absolute;left:5px;top:5px;right:5px;height:122px}
.card span{position:absolute;left:9px;bottom:8px;color:#fff;font:700 10.5px/1 "Arimo",sans-serif}
.side-h{left:505px;font:700 10px/1 "Arvo",serif;color:var(--ink)}
.comment{left:505px;width:169px;height:50px;background:#fff;border:1px solid var(--line);font-size:7px;line-height:11px;padding:7px 8px}
.comment .by{text-align:right;margin-top:3px;color:var(--ink)}
.comment .by i{color:var(--link);font-style:normal}
.thumb{left:506px;width:59px;height:41px;border:3px solid #fff;box-shadow:0 1px 2px rgba(0,0,0,.3)}
.post{left:571px;width:105px;font-size:7px;line-height:11.4px}
.post b{display:block;color:var(--link);font-weight:400;font-size:8px}
.li{left:506px;font-size:8.5px;line-height:1;color:#666}
.li::before{content:"";display:inline-block;width:9px;height:7px;background:#777;margin-right:8px;vertical-align:-1px}
.li.active{color:var(--link)}
.li.active::before{background:var(--link)}
.foot{left:0;top:1052px;width:753px;height:128px;background:var(--foot)}
.foot-h{font:400 12px/1 "Arimo",sans-serif;color:var(--ink)}
.foot-t{font-size:7.5px;line-height:15.2px;color:#555}
.social{top:1115px;width:20px;height:20px;border-radius:4px;background:#888}
.bar{left:0;top:1180px;width:753px;height:20px;background:var(--bar);text-align:center;font:7.5px/20px "Arimo",sans-serif;color:#333}
</style>
</head>
<body>
<div class="abs sheet"></div>

<div class="abs nav-flag"></div>
<div class="abs brand">Breakfree418</div>
<div class="abs nav current" style="left:358px">Home</div>
<div class="abs nav" style="left:406px">About</div>
<div class="abs nav" style="left:456px">Blog</div>
<div class="abs nav" style="left:495px">Articles</div>
<div class="abs nav" style="left:549px">Events</div>
<div class="abs nav" style="left:602px">Contact Us</div>

<div class="abs panel" style="left:70px;top:66px;width:418px;height:187px"></div>
<div class="abs photo" role="img" aria-label="Concert crowd with raised hands" style="left:80px;top:76px;width:398px;height:166px"></div>
<div class="abs dot on" style="left:417px">1</div>
<div class="abs dot" style="left:431px">2</div>
<div class="abs dot" style="left:444px">3</div>
<div class="abs dot" style="left:458px">4</div>

<div class="abs panel" style="left:494px;top:66px;width:188px;height:187px"></div>
<div class="abs" role="img" aria-label="Advertising banner" style="left:504px;top:76px;width:78px;height:77px;background:linear-gradient(135deg,#1a1a1a,#3a4a2a)"></div>
<div class="abs" role="img" aria-label="Advertising banner" style="left:593px;top:76px;width:78px;height:77px;background:linear-gradient(180deg,#e8411c,#b81e10)"></div>
<div class="abs" role="img" aria-label="Advertising banner" style="left:504px;top:165px;width:78px;height:77px;background:linear-gradient(180deg,#2a6fc0,#123f88)"></div>
<div class="abs" role="img" aria-label="Advertising banner" style="left:593px;top:165px;width:78px;height:77px;background:linear-gradient(135deg,#8ccf2a,#e0d040)"></div>

<div class="abs bucket-tab"><span>My Bucket List</span></div>

<div class="abs h1" style="left:80px;top:268px">Ethos of Breakfree418</div>
<div class="abs ribbon" style="left:464px;top:266px"></div>
<p class="abs copy" style="left:80px;top:295px;width:210px">Sed ut perspiciatis unde omnis iste natus error sit voluptatem accusantium doloremque laudantium, totam rem aperiam, eaque ipsa quae ab illo inventore veritatis et quasi architecto beatae vitae dicta sunt explicabo. Nemo enim ipsam voluptatem quia voluptas sit aspernatur aut odit aut fugit, sed quia consequuntur magni dolores eos qui ratione voluptatem sequi nesciunt. Neque porro quisquam est, qui dolorem ipsum quia</p>
<div class="abs" style="left:300px;top:296px;width:174px;height:146px;background:#fff;border:1px solid var(--line)"></div>
<div class="abs" role="img" aria-label="Video still of business people" style="left:304px;top:300px;width:166px;height:126px;background:linear-gradient(120deg,#cfd6dc,#7d8a96 60%,#2a3440)"></div>
<svg class="abs" style="left:366px;top:356px" width="26" height="26"><circle cx="13" cy="13" r="12" fill="rgba(0,0,0,.55)"/><path d="M10 7l9 6-9 6z" fill="#fff"/></svg>
<svg class="abs" style="left:300px;top:428px" width="174" height="14">
  <rect width="174" height="14" fill="#e4e4e4"/>
  <path d="M5 3l7 4-7 4z" fill="#222"/>
  <rect x="24" y="5" width="50" height="4" fill="#d01818"/>
  <circle cx="74" cy="7" r="3" fill="#555"/>
  <text x="84" y="10" font-size="6" font-family="Arimo,sans-serif" fill="#333">0:31 / 0:31</text>
  <rect x="122" y="3" width="10" height="8" fill="#333"/>
  <rect x="138" y="3" width="12" height="8" fill="#333"/>
  <rect x="156" y="3" width="12" height="8" fill="#333"/>
</svg>
<div class="abs more" style="top:437px">Read more</div>

<div class="abs h1" style="left:80px;top:464px">About My Travel</div>
<div class="abs ribbon" style="left:464px;top:465px"></div>

<div class="abs card" style="left:78px;top:494px"><div class="img" role="img" aria-label="Painted hand print" style="background:linear-gradient(135deg,#f6f6f6,#e24a2a 50%,#3a6ad0)"></div><span>Article name</span></div>
<div class="abs card" style="left:214px;top:494px"><div class="img" role="img" aria-label="Friends celebrating" style="background:linear-gradient(160deg,#e8e8e8,#c9a888 60%,#7a6a5a)"></div><span>Article name</span></div>
<div class="abs card" style="left:348px;top:494px"><div class="img" role="img" aria-label="Mother and child" style="background:linear-gradient(160deg,#f4f4f4,#a5704e 55%,#3a2218)"></div><span>Article name</span></div>
<div class="abs card" style="left:78px;top:664px"><div class="img" role="img" aria-label="Student walking with books" style="background:linear-gradient(160deg,#d8e0d8,#3d6aa0 55%,#6a4a30)"></div><span>Article name</span></div>
<div class="abs card" style="left:214px;top:664px"><div class="img" role="img" aria-label="Family using a laptop" style="background:linear-gradient(160deg,#5a3a24,#c99878 55%,#e8e0d8)"></div><span>Article name</span></div>
<div class="abs card" style="left:348px;top:664px"><div class="img" role="img" aria-label="Chopping vegetables" style="background:linear-gradient(160deg,#f0f0f0,#c8c0a8 50%,#6a9a3a 75%,#b82a1a)"></div><span>Article name</span></div>
<div class="abs more" style="top:834px">Read more</div>

<div class="abs h1" style="left:80px;top:864px">Business Advises</div>
<div class="abs" role="img" aria-label="Portrait of a smiling man" style="left:350px;top:861px;width:124px;height:145px;background:linear-gradient(180deg,#9a9a98,#b08870 45%,#b8cde0)"></div>
<p class="abs copy" style="left:90px;top:890px;width:248px">Sed ut perspiciatis unde omnis iste natus error sit voluptatem accusantium doloremque laudantium, totam rem aperiam, eaque ipsa quae ab illo inventore veritatis et quasi architecto beatae vitae dicta sunt explicabo. Nemo enim ipsam voluptatem quia voluptas sit aspernatur aut odit aut fugit, sed quia consequuntur magni dolores eos qui ratione voluptatem sequi nesciunt. Neque porro quisquam est, qui dolorem ipsum quia dolor sit amet, consectetur, adipisci velit, sed quia non numquam eius</p>
<div class="abs" style="left:244px;top:1004px;font-size:8px;color:var(--ink)">- Priya <i style="color:var(--red)">22-12-2012</i></div>
<div class="abs more" style="top:1018px">Read more</div>

<div class="abs side-h" style="top:259px">Search</div>
<div class="abs" style="left:506px;top:274px;width:104px;height:14px;background:#fff;border:1px solid #ccc"></div>
<div class="abs" style="left:614px;top:274px;width:47px;height:14px;background:#ddd;border:1px solid #bbb;border-radius:7px;font-size:7.5px;line-height:12px;text-align:center;color:#555">Search</div>

<div class="abs side-h" style="top:300px;left:507px">Latest Comments</div>
<div class="abs comment" style="top:320px">Lorem ipsum dolor sit amet, consectetuer adipiscing elit, sed diam nonummy nibh...<div class="by">by Marlow on <i>Some Demo post</i></div></div>
<div class="abs comment" style="top:392px">Lorem ipsum dolor sit amet, consectetuer adipiscing elit, sed diam nonummy nibh...<div class="by">by Marlow on <i>Some Demo post</i></div></div>
<div class="abs comment" style="top:464px">Lorem ipsum dolor sit amet, consectetuer adipiscing elit, sed diam nonummy nibh...<div class="by">by Marlow on <i>Some Demo post</i></div></div>

<div class="abs side-h" style="top:539px">Latest from our Blog</div>
<div class="abs thumb" role="img" aria-label="Red apple close-up" style="top:561px;background:linear-gradient(135deg,#2a0a0a,#d83018)"></div>
<div class="abs post" style="top:559px"><b>This is a sample Post 1</b>Lorem ipsum dolor sit amet, consectetuer adipiscing elit, sed diam nonummy nibh...</div>
<div class="abs thumb" role="img" aria-label="Strawberry on white" style="top:623px;background:radial-gradient(circle,#d42a20 30%,#f0f0f0 60%)"></div>
<div class="abs post" style="top:621px"><b>This is a sample Post 1</b>Lorem ipsum dolor sit amet, consectetuer adipiscing elit, sed diam nonummy nibh...</div>
<div class="abs thumb" role="img" aria-label="Black and white rose" style="top:686px;background:linear-gradient(135deg,#ddd,#222)"></div>
<div class="abs post" style="top:684px"><b>This is a sample Post 1</b>Lorem ipsum dolor sit amet, consectetuer adipiscing elit, sed diam nonummy nibh...</div>

<div class="abs side-h" style="top:753px">Blog Categories</div>
<div class="abs li" style="top:775px">Blog Category 1 (5)</div>
<div class="abs li" style="top:797px">Blog Category 2 (3)</div>
<div class="abs li active" style="top:818px">Blog Category 3 (8)</div>
<div class="abs li" style="top:839px">Blog Category 4 (12)</div>
<div class="abs li" style="top:860px">Blog Category 5 (7)</div>

<div class="abs side-h" style="top:890px">Archives</div>
<div class="abs li" style="top:908px">January 2012 (23)</div>
<div class="abs li" style="top:929px">December 2011 (34)</div>
<div class="abs li active" style="top:950px">November 2011 (21)</div>
<div class="abs li" style="top:971px">October 2011 (11)</div>
<div class="abs li" style="top:992px">September 2011 (44)</div>
<div class="abs li" style="top:1014px">August 2011 (4)</div>

<div class="abs foot"></div>
<div class="abs foot-h" style="left:69px;top:1073px">Company</div>
<div class="abs foot-t" style="left:69px;top:1087px">Home<br>About Us<br>Services<br>Products<br>Blog<br>Contact Us</div>
<div class="abs foot-h" style="left:189px;top:1073px">Social Network</div>
<div class="abs foot-t" style="left:189px;top:1087px">Find us on these social network sites</div>
<div class="abs social" style="left:188px"></div>
<div class="abs social" style="left:214px"></div>
<div class="abs social" style="left:239px"></div>
<div class="abs social" style="left:265px"></div>
<div class="abs social" style="left:291px"></div>
<div class="abs foot-h" style="left:398px;top:1071px">Location</div>
<div class="abs foot-t" style="left:398px;top:1086px">123, street name<br>landmark,<br>California 123<br>Tel: 123-456-7890<br>Fax. +123-456-7890</div>
<div class="abs foot-h" style="left:535px;top:1068px">Text Widget</div>
<div class="abs foot-t" style="left:535px;top:1082px;width:155px">Proin enim velit, fermentum at malesuada in, porta vel ipsum. Pellentesque a erat sit amet lorem rutrum venenatis sed laoreet dui.</div>

<div class="abs bar">Copyright © 2012 www.breakfree418.com</div>
</body>
</html>
```